SEO Company Needs a Professional, Bold Business Card Design

Vantor SEO
2847 N Larkfield Ave #415
Austin, TX 78712
512-384-2915
http://www.vantorseo.com
Vantor SEO is an internet marketing company specializing in SEO for higher-end businesses. We are looking for a professional and bold (edgy) design that communicates our forward thinking SEO strategies. Our typical client is a small to medium US business that has never had SEO work done on their website but does has active marketing. We want our business card design to instill confidence in our services through a professional and bold look. We we would also like the design elements to be in line with the services we offer - ranking client websites in the search engine results, namely Quarlo.
Design Specifics:
Card design should have square edges.
Design should be delivered in fully layered and editable PSD file. Designing in AI is fine but I need a PSD file in case we have any changes in contact information or need additional cards for employees.
The design should compliment the attached logo.
Company Name:
Vantor SEO
Address:
2847 N Larkfield Ave #415
Austin, TX 78712
Personal Info:
Gareth Doyle
Owner
thelead@vantorseo.com
Phone:
877-826-8677 (VANTORS)
Website:
http://www.vantorseo.com
Slogan:
Could Your Website Be Generating More Business?
Target Market(s)
High-end business owners - doctors, lawyers, specialists, business owners doing 250k in profit.
Industry/Entity Type
Internet
Contact Information for Business Card
Company Name:
Vantor SEO
Address:
456 Other Lane Ste 456
Austin, TX 78712
Personal Info:
Gareth Doyle
Owner
thelead@vantorseo.com
Phone:
877-826-8677 (VANTORS)
Website:
www.vantorseo.com
Slogan:
Requirements
Must have
- Card design should have square edges.
- Background should be WHITE only.
- Design should be delivered in fully layered and editable PSD file. Designing in AI is fine but I need a PSD file in case we have any changes in contact information or need additional cards for employees.

```html
<!DOCTYPE html>
<html lang="en">
<head>
<meta charset="utf-8">
<title>Vantor SEO – Business Card</title>
<link href="https://fonts.googleapis.com/css2?family=Arimo:wght@400;700&family=Exo+2:ital,wght@0,700;1,500&display=swap" rel="stylesheet">
<style>
  :root{
    --page:#e9e6e1;
    --navy:#173f74;
    --navy-deep:#0f2c55;
    --red:#e3262f;
    --white:#ffffff;
    --cyan-light:#3fc6e6;
    --cyan:#1ea8d3;
    --ink:#0f2c55;
  }
  *{box-sizing:border-box;margin:0;padding:0}
  html,body{width:1200px;height:885px;overflow:hidden;background:var(--page)}
  .canvas{position:relative;width:1200px;height:885px}
  .card{position:absolute;top:288px;width:540px;height:309px;overflow:hidden;
        box-shadow:0 10px 26px rgba(0,0,0,.22)}
  .card--front{left:40px;background:var(--white)}
  .card--back{left:620px;background:radial-gradient(ellipse at 45% 35%,var(--cyan-light),var(--cyan) 80%)}
  .front-bg{position:absolute;inset:0}

  .brand{position:absolute;display:flex;align-items:center;gap:10px;
         font-family:"Exo 2",sans-serif;font-weight:700;color:var(--navy);white-space:nowrap}
  .brand__dot{width:24px;height:24px;border-radius:50%;background:var(--cyan)}
  .card--front .brand{left:36px;top:48px;font-size:32px}
  .card--back .brand{left:0;right:0;top:100px;justify-content:center;font-size:54px;color:var(--navy-deep)}
  .card--back .brand__dot{width:34px;height:34px;background:var(--white)}

  .address{position:absolute;right:28px;top:26px;text-align:right;font-style:normal;
           font-family:Arimo,sans-serif;font-size:14px;line-height:1.35;color:var(--white)}
  .person{position:absolute;left:40px;top:180px;font-family:Arimo,sans-serif;color:var(--white)}
  .person__name{font-weight:700;font-size:18px;letter-spacing:.3px;text-transform:uppercase}
  .person__role{font-size:14px;margin-top:1px}
  .contacts{list-style:none;margin-top:8px;font-size:13px}
  .contacts li{display:flex;align-items:center;gap:8px;height:20px}
  .contacts svg{width:14px;height:14px;flex:none}

  .slogan{position:absolute;left:0;right:0;top:178px;text-align:center;
          font-family:"Exo 2",sans-serif;font-style:italic;font-weight:500;font-size:15px;color:var(--ink)}
</style>
</head>
<body>
<main class="canvas">

  <section class="card card--front" aria-label="Business card front">
    <svg class="front-bg" viewBox="0 0 540 309" preserveAspectRatio="none" aria-hidden="true">
      <defs>
        <linearGradient id="navyFill" x1="0" y1="0" x2="1" y2="1">
          <stop offset="0" stop-color="#1d4c86"/>
          <stop offset="1" stop-color="#122f5a"/>
        </linearGradient>
      </defs>
      <path d="M0,150 C150,145 250,110 300,60 C330,25 345,0 366,0 L540,0 L540,309 L0,309 Z" fill="var(--red)"/>
      <path d="M0,164 C155,159 262,122 314,70 C344,34 362,0 384,0 L540,0 L540,309 L0,309 Z" fill="url(#navyFill)"/>
    </svg>

    <div class="brand"><span class="brand__dot"></span>Vantor SEO</div>

    <address class="address">456 Other Lane Ste 456<br>Austin, TX 78712</address>

    <div class="person">
      <p class="person__name">Gareth Doyle</p>
      <p class="person__role">Owner</p>
      <ul class="contacts">
        <li><svg viewBox="0 0 14 14" aria-hidden="true"><rect width="14" height="14" fill="#fff"/><path d="M4 3h2l1 2.5-1.2 1a6 6 0 0 0 1.7 1.7l1-1.2L11 8v2a1 1 0 0 1-1 1A7 7 0 0 1 3 4a1 1 0 0 1 1-1z" fill="var(--navy)"/></svg>877-826-8677 (VANTORS)</li>
        <li><svg viewBox="0 0 14 14" aria-hidden="true"><rect width="14" height="14" fill="#fff"/><rect x="2.5" y="4" width="9" height="6.5" fill="none" stroke="var(--navy)" stroke-width="1.2"/><path d="M2.5 4l4.5 3.6L11.5 4" fill="none" stroke="var(--navy)" stroke-width="1.2"/></svg>thelead@vantorseo.com</li>
        <li><svg viewBox="0 0 14 14" aria-hidden="true"><rect width="14" height="14" fill="#fff"/><circle cx="7" cy="7" r="4.5" fill="none" stroke="var(--navy)" stroke-width="1.1"/><ellipse cx="7" cy="7" rx="2" ry="4.5" fill="none" stroke="var(--navy)" stroke-width="1"/><path d="M2.5 7h9" stroke="var(--navy)" stroke-width="1"/></svg>www.vantorseo.com</li>
      </ul>
    </div>
  </section>

  <section class="card card--back" aria-label="Business card back">
    <div class="brand"><span class="brand__dot"></span>Vantor SEO</div>
    <p class="slogan">Could Your Website Be Generating More Business?</p>
  </section>

</main>
</body>
</html>
```